Venture Capital Firm Needs Website Redesign

We need a bold revamp of our website (https://halvenmoor.vc/)
which at the moment looks washed out. We want a crisp, fresh and unique look. Feel free to keep as much or as little content in the site. The only thing we need to keep is a team section. The site should convey a clear distinction between our 3 product lines: Venture Capital, Private Credit, and Crypto. Two versions of our logo are attached and they should not change. For design inspirations, we like http://www.plumridgecap.com/ for a more simple site and for a more built out site we like http://tallowgate.com/

Updates
Industry/Entity Type
Investment
Coding
Coded - Design and coding required
Number of Pages Required
1 page
Font styles to use
Colors
Designer to choose colors to be used in the design.
Requirements
Must have
- - Clear distinction between our 3 product lines: Venture Capital, Private Credit
- - Team section

Nice to have
- Some really creative aspect like http://www.plumridgecap.com/ has with the distinction between first, second, and third kind

```html
<!DOCTYPE html>
<html lang="en">
<head>
<meta charset="utf-8">
<title>Halvenmoor — Venture Capital, Private Credit, Crypto</title>
<link rel="stylesheet" href="https://fonts.googleapis.com/css2?family=Arimo:wght@400;700&display=swap">
<style>
:root{
  --page:#ffffff;
  --panel:#f3f4ec;
  --panel-edge:#e6e7de;
  --ring:#f8f8f4;
  --green:#8ea51d;
  --chart-green:#b8c12a;
  --ink:#333333;
  --muted:#8a8a8a;
  --line:#cfcfcf;
  --button:#9a9a9a;
  --photo-a:#d9d9d9;
  --photo-b:#4a4a4a;
}
*{box-sizing:border-box;margin:0;padding:0}
html,body{width:1200px;height:1200px;overflow:hidden;background:var(--page)}
body{font-family:"Arimo",Arial,sans-serif;color:var(--ink)}
.canvas{position:relative;width:1200px;height:1200px;overflow:hidden;background:var(--page)}
.panel{position:absolute;background:var(--panel);overflow:hidden;box-shadow:0 1px 2px var(--panel-edge)}
.abs{position:absolute}
.wordmark{position:absolute;left:42px;top:9px;font-size:10.5px;letter-spacing:.4px;color:var(--ink)}
.nav-contact{position:absolute;left:690px;top:11px;font-size:5.5px;color:var(--ink)}
.ring{position:absolute;border-radius:50%;background:var(--ring);box-shadow:0 0 6px rgba(0,0,0,.06)}
.ring-brand{display:flex;align-items:center;justify-content:center;font-size:8px;letter-spacing:.6px;color:var(--ink);background:#fff}
.arrow{position:absolute;width:24px;height:24px;border:1px solid #555;display:flex;align-items:center;justify-content:center;font-size:9px;color:#333;background:transparent}
.section-title{position:absolute;font-size:13.5px;color:var(--green);font-weight:400;letter-spacing:.2px}
.copy{position:absolute;font-size:5.3px;line-height:7.9px;color:var(--ink)}
.portfolio-tile{position:absolute;height:27px;background:#fafaf6;display:flex;align-items:center;justify-content:center;font-size:8px;color:var(--muted)}
.btn{position:absolute;background:var(--button);color:#fff;font-size:5px;display:flex;align-items:center;justify-content:center}
.modal{position:absolute;left:0;top:894px;width:756px;height:240px;background:#fff}
.modal .label{position:absolute;font-size:5px;font-weight:700;color:var(--ink)}
.modal .field{position:absolute;border:1px solid var(--line);font-size:4.8px;color:#aaa;padding:3px 5px}
.close{position:absolute;left:723px;top:899px;font-size:12px;color:#aaa}
.photo{position:absolute;background:linear-gradient(160deg,var(--photo-a),var(--photo-b))}
.scrollbar{position:absolute;left:826px;top:1092px;width:374px;height:5px;background:#e8e8e2}
.scrollbar span{position:absolute;left:6px;top:1px;width:36px;height:3px;background:#c8c8c2}
</style>
</head>
<body>
<div class="canvas">

  <!-- Hero -->
  <section class="panel" style="left:0;top:0;width:756px;height:376px">
    <div class="wordmark">HALVENMOOR</div>
    <div class="nav-contact">Contact</div>
    <div class="ring" style="left:261px;top:72px;width:236px;height:236px"></div>
    <div class="ring" style="left:309px;top:120px;width:140px;height:140px"></div>
    <div class="ring ring-brand" style="left:336px;top:147px;width:86px;height:86px">HALVENMOOR</div>
    <div class="arrow" style="left:623px;top:178px">‹</div>
    <div class="arrow" style="left:656px;top:178px">›</div>
  </section>

  <!-- Venture capital -->
  <section class="panel" style="left:0;top:376px;width:756px;height:376px">
    <div class="wordmark">HALVENMOOR</div>
    <div class="nav-contact">Contact</div>
    <h2 class="section-title" style="left:165px;top:109px">VENTURE CAPITAL</h2>
    <p class="copy" style="left:165px;top:127px;width:165px">We invest in early-stage startups led by founders who are passionate and knowledgeable about the markets they serve. We have our own software developers and product managers. We work with the founders in our portfolio to help them bring products to market, earning equity for this work and for the cash we invest in their companies.</p>
    <div class="portfolio-tile" style="left:165px;top:183px;width:58px;font-size:5px">ARDENT GROUP</div>
    <div class="portfolio-tile" style="left:228px;top:183px;width:58px;font-size:6px">pixelkind</div>
    <div class="portfolio-tile" style="left:290px;top:183px;width:59px;font-size:9px">tinyroute</div>
    <div class="portfolio-tile" style="left:354px;top:183px;width:58px;font-size:7px">Loomline</div>
    <div class="arrow" style="left:623px;top:178px">‹</div>
    <div class="arrow" style="left:656px;top:178px">›</div>
  </section>

  <!-- Contact -->
  <section class="panel" style="left:0;top:752px;width:756px;height:382px">
    <div class="wordmark">HALVENMOOR</div>
    <div class="nav-contact">Contact</div>
    <div class="ring" style="left:261px;top:70px;width:236px;height:236px"></div>
    <div class="ring" style="left:309px;top:118px;width:140px;height:140px"></div>
  </section>

  <div class="modal">
    <h2 class="section-title" style="left:26px;top:36px">CONTACT US</h2>
    <p class="copy" style="left:26px;top:52px">We would love to hear from you.</p>
    <p class="copy" style="left:26px;top:63px;font-weight:700">info@halvenmoor.vc</p>
    <p class="copy" style="left:26px;top:75px">212 Mercer Street, Suite 410</p>
    <p class="copy" style="left:26px;top:87px">New York, NY</p>
    <p class="copy" style="left:26px;top:99px">10012</p>
    <span class="label" style="left:382px;top:22px">Name:</span>
    <div class="field" style="left:382px;top:30px;width:350px;height:14px">Enter your name</div>
    <span class="label" style="left:382px;top:52px">Email Address:</span>
    <div class="field" style="left:382px;top:59px;width:350px;height:14px">Enter your email</div>
    <div class="field" style="left:382px;top:77px;width:350px;height:118px">Message</div>
    <span class="label" style="left:388px;top:207px;font-weight:400">Submit</span>
  </div>
  <div class="close">×</div>

  <!-- Crypto -->
  <section class="panel" style="left:756px;top:38px;width:444px;height:372px">
    <h2 class="section-title" style="left:48px;top:109px">CRYPTO</h2>
    <p class="copy" style="left:48px;top:128px;width:165px">The Halvenmoor Crypto Index tracks the top 15 cryptocurrencies weighted by market cap and rebalanced twice a month. We believe this is the simplest and most cost effective way to obtain cryptocurrency exposure. Our process has been designed by experts from financial services and cryptocurrency industries.</p>
    <div class="btn" style="left:46px;top:173px;width:41px;height:19px">Learn more</div>
    <svg class="abs" style="left:244px;top:102px" width="200" height="220" viewBox="0 0 200 220" role="img" aria-label="Line chart of cumulative growth, index against benchmark">
      <g font-family="Arimo, Arial, sans-serif" font-weight="700" fill="#333">
        <text x="121" y="4" font-size="4.2" text-anchor="middle">HCI Cumulative Growth</text>
        <circle cx="90" cy="15" r="3.2" fill="var(--chart-green)"/>
        <text x="96" y="17" font-size="4">HCI (1236.48%)</text>
        <circle cx="140" cy="15" r="3.2" fill="#111"/>
        <text x="146" y="17" font-size="4">Benchmark (717.41%)</text>
        <g font-size="3.8" text-anchor="end">
          <text x="34" y="25">3500</text><text x="34" y="43">3000</text><text x="34" y="62">2500</text>
          <text x="34" y="80">2000</text><text x="34" y="99">1500</text><text x="34" y="117">1000</text>
          <text x="34" y="136">500</text><text x="34" y="154">0</text>
        </g>
        <g font-size="3.8" text-anchor="middle">
          <text x="39" y="160">Jan</text><text x="51" y="160">Feb</text><text x="63" y="160">Mar</text>
          <text x="76" y="160">Apr</text><text x="88" y="160">May</text><text x="100" y="160">Jun</text>
          <text x="113" y="160">Jul</text><text x="125" y="160">Aug</text><text x="138" y="160">Sep</text>
          <text x="150" y="160">Oct</text><text x="162" y="160">Nov</text><text x="175" y="160">Dec</text>
          <text x="187" y="160">Jan</text><text x="199" y="160">Feb</text>
        </g>
        <text x="28" y="167" font-size="2.6" font-weight="400">Chart shown for information only; past returns do not predict future results.</text>
        <text x="193" y="175" font-size="2.6" font-weight="400" fill="#2255cc" text-decoration="underline">more</text>
      </g>
      <polyline fill="none" stroke="#111" stroke-width="1" points="36,153 42.2,153 48.4,152.8 54.6,152.6 60.8,152.4 67,152.3 73.2,151.9 79.4,150.8 85.6,149.3 91.8,147.4 98,148.5 104.2,145.6 110.4,146.3 116.6,141.9 122.8,142.6 129,138.1 135.2,138.9 141.4,134.4 147.6,135.2 153.8,130.7 160,119.6 166.2,82.4 172.4,93.6 178.6,108.4 184.8,119.6 191,124"/>
      <polyline fill="none" stroke="var(--chart-green)" stroke-width="1.2" points="36,153 42.2,153 48.4,152.6 54.6,152.3 60.8,151.9 67,151.5 73.2,150.8 79.4,148.5 85.6,145.6 91.8,141.9 98,143.7 104.2,138.9 110.4,137.4 116.6,130.7 122.8,134.4 129,127 135.2,128.9 141.4,119.6 147.6,121.4 153.8,112.1 160,101 166.2,75 172.4,65.7 178.6,37.9 184.8,56.4 191,62"/>
      <g fill="var(--chart-green)">
        <circle cx="36" cy="153" r="1"/><circle cx="48.4" cy="152.6" r="1"/><circle cx="60.8" cy="151.9" r="1"/><circle cx="73.2" cy="150.8" r="1"/><circle cx="85.6" cy="145.6" r="1"/><circle cx="98" cy="143.7" r="1"/><circle cx="110.4" cy="137.4" r="1"/><circle cx="122.8" cy="134.4" r="1"/><circle cx="135.2" cy="128.9" r="1"/><circle cx="147.6" cy="121.4" r="1"/><circle cx="160" cy="101" r="1"/><circle cx="172.4" cy="65.7" r="1"/><circle cx="178.6" cy="37.9" r="1"/>
      </g>
    </svg>
  </section>

  <!-- Private credit -->
  <section class="panel" style="left:756px;top:413px;width:444px;height:371px">
    <h2 class="section-title" style="left:44px;top:108px">PRIVATE CREDIT</h2>
    <p class="copy" style="left:44px;top:127px;width:160px">Halvenmoor Private Credit provides capital to lending businesses that are focused on using technology to establish new credit markets, create new credit products or dramatically re-invent an existing form of credit. We believe that the pioneers who build something truly different in a credit market will create the most sustainable business models. Given our heritage as a venture firm, we are comfortable with emerging businesses and can provide capital for a company's first loan.</p>
    <div class="portfolio-tile" style="left:44px;top:199px;width:61px;font-size:8px;font-weight:700">NORVALE</div>
    <div class="portfolio-tile" style="left:108px;top:199px;width:58px"><span style="display:block;width:12px;height:12px;border-radius:50%;background:#9a9a9a"></span></div>
    <div class="portfolio-tile" style="left:170px;top:199px;width:59px;font-size:7.5px">BRIGHTLEND</div>
  </section>

  <!-- Team -->
  <section class="panel" style="left:756px;top:786px;width:444px;height:358px">
    <h2 class="section-title" style="left:70px;top:76px">OUR TEAM</h2>
    <p class="copy" style="left:70px;top:93px">The very best helping the very best.</p>
  </section>
  <div class="photo" style="left:826px;top:895px;width:158px;height:196px" role="img" aria-label="Black and white portrait of a team member"></div>
  <div class="photo" style="left:988px;top:895px;width:157px;height:196px" role="img" aria-label="Black and white portrait of a team member"></div>
  <div class="photo" style="left:1149px;top:895px;width:60px;height:196px" role="img" aria-label="Black and white portrait of a team member"></div>
  <div class="scrollbar"><span></span></div>

</div>
</body>
</html>
```